Business Card Design for a Technology Development Company

******* PLEASE NOTE (ALL DESIGNERS): I am going to finish the competition on Monday the 9th July (NOT SATURDAY 15TH). I have some designs I like and need to get them printed next week. Please submit any designs today or tomorrow. *******

PLEASE READ ALL OF THE REQUIREMENTS!!! I've rejected lot's of designs in the past because they didn't read the basic requirements - thanks and good luck!

Quill Harbor is a UK technology / small holding company that invests in startups and develops new ideas. In addition it provides IT Professional Services.

Ideally the design will be simple, professional, smart, and sophisticated, and overall be nice to look at. You can be creative as you like with the design, equally as simple as you like - you guys are the professionals so I'll leave it to your inspiration (make sure you incorporate the logo)!
Updates

PLEASE NOTE (ALL DESIGNERS): I am going to finish the competition on Monday the 9th July (NOT SATURDAY 15TH).  I have some designs I like and need to get them printed next week.  Please submit any designs today or tomorrow.

Target Market(s)

Enterprises / corporations / public sector / technical engineers / investors. More www.brontavex.com / www.pelmora.com than www.flinkaro.com!

Industry/Entity Type

Business

Requirements
Must have
• It should be modern and any artwork (if used) should be simple
- Pastel colours, dark and light colours, and shades are preferred over bright colours
- The design should incorporate the attached Quill Harbor logo and the logo colour scheme
- The logo should be on both sides. The back should just have the logo, maybe with some additional graphics
- It must have the following information on:

FirstName SecondName
Company Position
Email: name@quillharbor.co.uk
Mobile: +44 (0) 7700 900482

- The final design should be for a UK business card, dimensions: 85mm × 55mm
- The final design should have bleed marks to allow for printing and should be given in vector formats (EPS and AI)
Nice to have
• The Logo can be separated from the font in the logo on the front of the card. This isn't necessary or required, just to know it's not a limitation.
Should not have
• No bright colours (I prefer pastel colours, dark and light colours, and shades)
- Fonts that are to thin
- Effects or designs that make it difficult to print
- Italic or old fashioned looking fonts, i.e. anything like Times New Roman is a NO!

```html
<!DOCTYPE html>
<html lang="en">
<head>
<meta charset="utf-8">
<title>Quill Harbor – Business Card</title>
<link rel="stylesheet" href="https://fonts.googleapis.com/css2?family=Source+Sans+3:wght@400;600&display=swap">
<style>
  :root {
    --backdrop: #e8e6e3;
    --teal: #0b8ea9;
    --teal-soft: #2ea4bb;
    --aqua-light: #8fd8e8;
    --aqua-band: #7fd0e2;
    --white: #ffffff;
    --ink-teal: #0d7f98;
  }
  * { box-sizing: border-box; margin: 0; padding: 0; }
  html, body {
    width: 1200px; height: 508px; overflow: hidden;
    background: var(--backdrop);
    font-family: "Source Sans 3", "Helvetica Neue", Arial, sans-serif;
  }
  .stage { position: relative; width: 1200px; height: 508px; }
  .card {
    position: absolute; top: 96px; width: 488px; height: 316px;
    border-radius: 36px; overflow: hidden;
  }
  .card-back { left: 82px; background: var(--teal); }
  .card-front { left: 632px; background: var(--white); }

  .brand { position: absolute; display: flex; align-items: center; gap: 14px; font-weight: 600; letter-spacing: -0.5px; }
  .brand-dot { width: 34px; height: 34px; border-radius: 50%; }
  .card-back .brand { left: 50px; top: 130px; font-size: 42px; color: var(--white); }
  .card-back .brand-dot { background: var(--aqua-light); }
  .card-front .brand { left: 34px; top: 44px; font-size: 40px; color: var(--ink-teal); }
  .card-front .brand-dot { background: var(--teal-soft); }

  .website {
    position: absolute; left: 0; right: 0; top: 268px; text-align: center;
    font-size: 16px; letter-spacing: 0.6px; color: var(--white);
  }
  .front-waves { position: absolute; inset: 0; }
  .person { position: absolute; right: 32px; top: 130px; text-align: right; }
  .person-name { font-size: 22px; font-weight: 600; color: var(--aqua-light); line-height: 1.1; }
  .person-role { font-size: 17px; color: var(--white); margin-top: 2px; }
  .contact { position: absolute; left: 34px; top: 248px; list-style: none; }
  .contact li { display: flex; align-items: center; gap: 10px; font-size: 19px; color: var(--white); height: 29px; }
  .contact svg { width: 20px; height: 16px; flex: none; }
</style>
</head>
<body>
<main class="stage">
  <section class="card card-back" aria-label="Card back">
    <div class="brand"><span class="brand-dot"></span>Quill Harbor</div>
    <p class="website">www.quillharbor.co.uk</p>
  </section>

  <section class="card card-front" aria-label="Card front">
    <svg class="front-waves" viewBox="0 0 488 316" preserveAspectRatio="none" aria-hidden="true">
      <path d="M0,128 C110,150 230,152 300,140 C230,160 110,166 0,160 Z" fill="var(--aqua-band)"/>
      <path d="M0,158 C160,176 360,150 488,54 L488,316 L0,316 Z" fill="var(--teal)"/>
    </svg>
    <div class="brand"><span class="brand-dot"></span>Quill Harbor</div>
    <div class="person">
      <p class="person-name">Marcus Hale</p>
      <p class="person-role">manager</p>
    </div>
    <ul class="contact">
      <li>
        <svg viewBox="0 0 20 16" aria-hidden="true">
          <rect x="1" y="1" width="18" height="14" rx="2" fill="var(--aqua-light)"/>
          <rect x="3" y="3" width="5" height="10" rx="1" fill="var(--teal)"/>
          <rect x="10" y="3" width="7" height="3" fill="var(--teal)"/>
          <rect x="10" y="8" width="3" height="2" fill="var(--teal)"/>
          <rect x="14" y="8" width="3" height="2" fill="var(--teal)"/>
          <rect x="10" y="11" width="3" height="2" fill="var(--teal)"/>
          <rect x="14" y="11" width="3" height="2" fill="var(--teal)"/>
        </svg>
        +44 (0) 7700 900482
      </li>
      <li>
        <svg viewBox="0 0 20 16" aria-hidden="true">
          <rect x="1" y="2" width="18" height="12" rx="1" fill="var(--aqua-light)"/>
          <path d="M1.5,3 L10,9.5 L18.5,3" fill="none" stroke="var(--teal)" stroke-width="1.4"/>
        </svg>
        name@quillharbor.co.uk
      </li>
    </ul>
  </section>
</main>
</body>
</html>
```